Business Cards for a law firm

Business cards for our law firm. Use our silhoette logo and OAK HARBOR - check our website (www.oakharbor-legal.com)

Contact Information for Business Card

our silhouette logo, OAK HARBOR, 800-555-0147, Dorian Kestrup, dorian@oakharbor-legal.com

Requirements
Must have
• our silhouette logo, OAK HARBOR, 800-555-0147, Dorian Kestrup, dorian@oakharbor-legal.com

```html
<!DOCTYPE html>
<html lang="en">
<head>
<meta charset="utf-8">
<title>Oak Harbor Business Cards</title>
<link href="https://fonts.googleapis.com/css2?family=Oswald:wght@400;500;600&display=swap" rel="stylesheet">
<style>
  :root {
    --navy: #1b2f6b;
    --navy-deep: #162859;
    --gold: #e9a21f;
    --white: #ffffff;
    --paper: #f4f4f4;
    --stage: #3a3a3a;
  }
  * { margin: 0; padding: 0; box-sizing: border-box; }
  html, body { width: 1200px; height: 900px; overflow: hidden; }
  body {
    background: var(--stage);
    font-family: "Oswald", sans-serif;
    position: relative;
  }
  .card {
    position: absolute;
    left: 320px;
    width: 560px;
    height: 320px;
    background: var(--white);
    overflow: hidden;
    box-shadow: 0 8px 22px rgba(0,0,0,0.45);
  }
  .card--front { top: 90px; background: linear-gradient(160deg, var(--white), var(--paper)); }
  .card--back { top: 470px; }

  .brand {
    position: absolute;
    display: flex;
    align-items: center;
    gap: 16px;
  }
  .brand__mark {
    width: 22px;
    height: 22px;
    background: var(--navy);
  }
  .brand__name {
    color: var(--navy);
    font-weight: 500;
    font-size: 30px;
    letter-spacing: 5px;
    line-height: 1;
  }
  .card--front .brand { left: 130px; top: 142px; }
  .card--back .brand { left: 60px; top: 58px; }

  .back__band {
    position: absolute;
    left: 0; right: 0; top: 122px; bottom: 0;
    background: linear-gradient(170deg, var(--navy), var(--navy-deep));
  }
  .contact {
    position: absolute;
    left: 170px;
    width: 320px;
    top: 134px;
    text-align: center;
    color: var(--white);
  }
  .contact__name {
    font-size: 34px;
    font-weight: 600;
    line-height: 1.1;
    text-transform: uppercase;
  }
  .contact__email {
    color: var(--gold);
    font-size: 17px;
    font-weight: 500;
    line-height: 1.2;
  }
  .contact__phone {
    font-size: 38px;
    font-weight: 500;
    line-height: 1.1;
  }
  .contact__rule {
    width: 62px;
    height: 3px;
    background: var(--gold);
    margin: 10px auto 16px;
  }
  .contact__web {
    font-size: 20px;
    font-weight: 500;
    line-height: 1.2;
  }
</style>
</head>
<body>
  <section class="card card--front">
    <div class="brand">
      <span class="brand__mark"></span>
      <span class="brand__name">OAK HARBOR</span>
    </div>
  </section>

  <section class="card card--back">
    <div class="back__band"></div>
    <div class="brand">
      <span class="brand__mark"></span>
      <span class="brand__name">OAK HARBOR</span>
    </div>
    <div class="contact">
      <p class="contact__name">Dorian Kestrup</p>
      <p class="contact__email">dorian@oakharbor-legal.com</p>
      <p class="contact__phone">800-555-0147</p>
      <div class="contact__rule"></div>
      <p class="contact__web">www.oakharbor-legal.com</p>
    </div>
  </section>
</body>
</html>
```